Digital Marketing Website Design

I need the homepage designed for my new digital marketing agency I am starting. The main goal for this homepage is to drive people to make an appointment for me to discuss their upcoming projects. Here are some examples of the layouts that I would like to emulate.
https://www.tallmarsh.com/
https://www.quillforge.com/
https://pebblenook.com/
https://drvenholt.com/
https://www.quietlyrooted.org/
My main focus is to attract leads that need help with running digital ads such as Chatterly ads and Finder Promos. I do offer other services like SEO and other things but the main focus is digital Ads.
The final design should communicate Orchid Digital is a Digital marketing strategist building predictable revenue for small businesses through digital ads, email and marketing automation.
Target Market(s)
30-55, business owners, income 100K+, ecommerce companies, etc.
Industry/Entity Type
Digital Marketing
Number of Pages Required
2 page
Font styles to use
Requirements
Must have
- An appealing look and feel set to drive people to make an appointment.
Logo
There needs to be a call to action button in the far right of the navigation
The same call to action in the navigation needs to be in each section on the homepage.
I need the homepage and an about us page.

```html
<!DOCTYPE html>
<html lang="en">
<head>
<meta charset="utf-8">
<title>Orchid Digital — Profitable Ad Campaigns For Small Businesses</title>
<link rel="stylesheet" href="https://fonts.googleapis.com/css2?family=Poppins:wght@400;500;600&family=Montserrat:wght@400;500;600&display=swap">
<style>
:root{
  --orange:#f05a28;
  --orange-soft:#fde6dc;
  --ink:#17223a;
  --body:#4a4f5c;
  --black:#111111;
  --grey-band:#eeeeef;
  --white:#ffffff;
  --footer:#1d2128;
}
*{box-sizing:border-box;margin:0;padding:0}
html,body{width:1200px;height:3710px;overflow:hidden}
body{font-family:"Montserrat",sans-serif;color:var(--body);background:var(--white);position:relative}
section,header,footer{position:relative;width:1200px}
.abs{position:absolute}
.center{left:0;width:1200px;text-align:center}
h1,h2,h3{font-family:"Poppins",sans-serif;font-weight:400;color:var(--ink)}
.section-title{font-size:31px}
.rule{position:absolute;left:565px;width:70px;height:3px;background:var(--orange)}
.btn{position:absolute;display:flex;align-items:center;justify-content:center;gap:8px;font-family:"Montserrat",sans-serif;font-weight:600;font-size:17px;border-radius:3px;text-decoration:none;white-space:nowrap}
.btn-dark{background:var(--black);color:var(--orange);border:2px solid #2a2a2a}
.btn-orange{background:var(--orange);color:var(--white)}
.btn .dot{width:10px;height:10px;border-radius:50%;background:currentColor;opacity:.9}

/* nav */
.site-nav{height:73px;background:var(--white);box-shadow:0 1px 4px rgba(0,0,0,.08)}
.brand{display:flex;align-items:center;gap:6px;font-family:"Poppins",sans-serif;font-weight:600;font-size:23px;letter-spacing:.5px;color:var(--ink);white-space:nowrap}
.brand .mark{width:14px;height:14px;background:var(--orange)}
.nav-link{font-family:"Poppins",sans-serif;font-size:18px;color:var(--ink);top:26px}
.nav-link.active{color:var(--orange)}

/* hero */
.hero{height:544px;background:linear-gradient(120deg,#2b2e33 0%,#51555b 40%,#3c3f44 70%,#1f2226 100%)}
.hero-title{color:var(--white);font-size:46px;line-height:49px}
.hero-title em{font-style:normal;color:var(--orange)}
.hero-sub{left:200px;width:800px;text-align:center;color:var(--white);font-size:18px;line-height:28px;font-family:"Poppins",sans-serif}

/* featured */
.featured{height:282px}
.press-box{top:126px;width:130px;height:80px;background:var(--white);box-shadow:0 2px 8px rgba(0,0,0,.12);display:flex;align-items:center;justify-content:center;font-family:"Poppins",sans-serif;font-size:18px;color:#555}

/* services */
.services{height:590px;background:radial-gradient(ellipse at center,#fafafa 0%,var(--grey-band) 80%)}
.service-card{top:166px;width:283px;height:287px;background:var(--white);border-radius:10px;box-shadow:0 4px 14px rgba(0,0,0,.06);text-align:center}
.icon-ring{position:absolute;left:91px;top:36px;width:100px;height:100px;border-radius:50%;background:var(--orange-soft);box-shadow:0 3px 8px rgba(0,0,0,.12);display:flex;align-items:center;justify-content:center}
.service-card h3{position:absolute;top:164px;width:100%;font-size:17px;font-weight:500}
.service-card p{position:absolute;top:198px;left:30px;right:30px;font-size:13px;line-height:20px}

/* how */
.how{height:853px}
.how p.copy{font-size:14px;line-height:22.5px;color:var(--body)}
.step-ring{top:366px;width:120px;height:120px}
.step-label{font-family:"Poppins",sans-serif;color:var(--orange);font-size:17px;top:498px;width:280px;text-align:center}
.step-text{top:524px;width:270px;text-align:center;font-size:14px;line-height:22.5px}

/* testimonials */
.testimonials{height:486px;background:linear-gradient(100deg,#1a2230 0%,#2e3542 45%,#1e2530 100%)}
.testimonials h2{color:var(--white);font-weight:600;font-size:31px}
.quote-card{top:195px;width:296px;height:203px;background:var(--white)}
.quote-card .qm{position:absolute;left:14px;top:10px;font-family:"Poppins",sans-serif;font-size:44px;color:#d9dbe0;line-height:1}
.quote-card p{position:absolute;left:14px;right:14px;top:46px;font-size:11px;line-height:19px}
.avatar{position:absolute;right:22px;top:-28px;width:64px;height:64px;border-radius:50%;border:3px solid var(--orange);background:linear-gradient(160deg,#c9b3a4,#7c6a5f)}
.name-tag{position:absolute;left:0;top:162px;width:135px;height:26px;background:var(--orange);color:var(--white);font-size:12px;line-height:26px;padding-left:14px;border-radius:0 14px 14px 0}
.stars{position:absolute;right:24px;top:164px;color:var(--orange);font-size:13px;letter-spacing:3px}
.stars .off{color:#999}
.slider-arrow{top:281px;width:42px;height:42px;border-radius:50%;display:flex;align-items:center;justify-content:center;font-size:12px}

/* why */
.why{height:547px}
.why-card{top:202px;width:287px;height:203px;background:var(--white);box-shadow:0 3px 12px rgba(0,0,0,.1);text-align:center}
.why-icon{position:absolute;left:98px;top:-46px;width:90px;height:90px;border-radius:50%;border:2px solid var(--orange);background:var(--white);display:flex;align-items:center;justify-content:center}
.why-card h3{position:absolute;top:64px;width:100%;font-size:17px;font-weight:500}
.why-card p{position:absolute;top:98px;left:12px;right:12px;font-size:13px;line-height:20.5px}

/* footer */
.site-footer{height:293px;background:linear-gradient(90deg,#1a1e24,#2a3038 60%,#1c2026)}
.site-footer h4{font-family:"Poppins",sans-serif;font-weight:400;font-size:18px;color:var(--white)}
.site-footer li{list-style:none;font-size:13px;color:var(--white);line-height:26px}
.contact-item{display:flex;gap:10px;color:var(--white);font-size:12.5px;line-height:17px;white-space:nowrap}
.social{width:24px;height:24px;border-radius:50%;background:var(--orange);border:2px solid #ffb08f}
.copyright{height:42px;background:var(--orange);color:var(--white);font-size:12.5px;line-height:42px;text-align:center}
</style>
</head>
<body>

<header class="site-nav">
  <div class="brand abs" style="left:110px;top:24px"><span class="mark"></span>ORCHIDDIGITAL</div>
  <a class="nav-link active abs" style="left:518px">Home</a>
  <a class="nav-link abs" style="left:610px">About Us</a>
  <a class="nav-link abs" style="left:733px">Case Studies</a>
  <a class="btn btn-dark" style="left:860px;top:18px;width:235px;height:42px"><span class="dot"></span>Schedule Appointment</a>
</header>

<section class="hero" role="img" aria-label="Photo of a team celebrating a win around an office table">
  <h1 class="hero-title abs center" style="top:164px">We Built <em>Profitable Ad Campaigns</em><br>For Small Businesses</h1>
  <p class="hero-sub abs" style="top:267px">The Selling System That Brings In Predictable Revenue Through Digital Ads, Email And Marketing Automation</p>
  <a class="btn btn-orange" style="left:331px;top:334px;width:290px;height:41px"><span class="dot"></span>Free Chatterly Ads Checklist</a>
  <a class="btn btn-dark" style="left:634px;top:334px;width:234px;height:41px"><span class="dot"></span>Schedule Appointment</a>
</section>

<section class="featured">
  <h2 class="section-title abs center" style="top:36px">As Featured On</h2>
  <div class="rule" style="top:88px"></div>
  <div class="press-box abs" style="left:140px">Larkfield</div>
  <div class="press-box abs" style="left:297px">Larkfield</div>
  <div class="press-box abs" style="left:455px">Presswell</div>
  <div class="press-box abs" style="left:612px">Dotbloom</div>
  <div class="press-box abs" style="left:770px">Tilemark</div>
  <div class="press-box abs" style="left:927px">Tilemark</div>
</section>

<section class="services">
  <h2 class="section-title abs center" style="top:78px">OrchidDigital Featured Services</h2>
  <div class="rule" style="top:127px"></div>

  <article class="service-card abs" style="left:141px">
    <div class="icon-ring">
      <svg width="50" height="50" viewBox="0 0 50 50" fill="none" stroke="#f05a28" stroke-width="2.5" stroke-linejoin="round"><path d="M8 20h8l18-10v30L16 30H8z"/><path d="M16 30l4 12h6l-3-12"/><path d="M40 18v14"/></svg>
    </div>
    <h3>Chatterly Ads</h3>
    <p>Lorem ipsum dolor sit amet, consectetuer adipiscing elit, sed diam nonummy nibh euismod</p>
  </article>

  <article class="service-card abs" style="left:459px">
    <div class="icon-ring" style="background:var(--orange)"></div>
    <h3 style="color:var(--orange)">Finder Promos</h3>
    <p>Lorem ipsum dolor sit amet, consectetuer adipiscing elit, sed diam nonummy nibh euismod</p>
  </article>

  <article class="service-card abs" style="left:776px">
    <div class="icon-ring">
      <svg width="54" height="54" viewBox="0 0 54 54" fill="none" stroke="#f05a28" stroke-width="2.5"><rect x="6" y="10" width="22" height="15"/><path d="M6 10l11 9 11-9"/><circle cx="34" cy="33" r="11"/><circle cx="34" cy="33" r="4"/></svg>
    </div>
    <h3>Email &amp; Marketing Automation</h3>
    <p>Lorem ipsum dolor sit amet, consectetuer adipiscing elit, sed diam nonummy nibh euismod</p>
  </article>

  <a class="btn btn-dark" style="left:490px;top:490px;width:235px;height:41px"><span class="dot"></span>Schedule Appointment</a>
</section>

<section class="how">
  <h2 class="section-title abs center" style="top:68px">How It Works</h2>
  <p class="copy abs" style="left:150px;width:900px;top:130px;text-align:center">At Orchid Digital Solutions we know that you want to have a profitable business. In order to do that, you need a strong system that can predictably bring in sales even in bad times. The problem is there is so much out there to wade through and so many people telling you what you should do which makes you feel frustrated, lost, and flat out stressed out. We believe that businesses with great products should get the customer.</p>
  <p class="copy abs" style="left:150px;width:900px;top:238px;text-align:center">We understand the frustration which is why we are here to help you maneuver through the minutiae and create a system that flat out works.</p>
  <p class="abs center" style="top:312px;color:var(--orange);font-size:15px">Here's How We Do It:</p>

  <svg class="step-ring abs" style="left:238px" viewBox="0 0 120 120"><circle cx="60" cy="60" r="54" fill="#f1f1f3"/><path d="M60 4a56 56 0 0 1 40 95" fill="none" stroke="#f05a28" stroke-width="2"/><path d="M20 100A56 56 0 0 1 40 8" fill="none" stroke="#f05a28" stroke-width="2"/><g fill="none" stroke="#444" stroke-width="1.8"><rect x="36" y="38" width="44" height="38" rx="2"/><path d="M36 48h44M44 34v8M72 34v8M44 56h6M56 56h6M68 56h6M44 65h6M56 65h6"/><circle cx="78" cy="76" r="8"/><path d="M74 76l3 3 5-6"/></g></svg>
  <svg class="abs" style="left:412px;top:420px" width="90" height="12"><path d="M0 6h80" stroke="#999" stroke-dasharray="3 3"/><path d="M78 1l8 5-8 5" fill="#999"/></svg>
  <svg class="step-ring abs" style="left:550px" viewBox="0 0 120 120"><circle cx="60" cy="60" r="54" fill="#f1f1f3"/><path d="M60 4a56 56 0 0 1 40 95" fill="none" stroke="#f05a28" stroke-width="2"/><path d="M20 100A56 56 0 0 1 40 8" fill="none" stroke="#f05a28" stroke-width="2"/><g fill="none" stroke="#444" stroke-width="1.8"><circle cx="60" cy="40" r="7"/><path d="M60 50v8M40 62h40M40 62v6M60 58v10M80 62v6"/><circle cx="40" cy="74" r="5"/><circle cx="60" cy="74" r="5"/><circle cx="80" cy="74" r="5"/><path d="M32 88a8 8 0 0 1 16 0M52 88a8 8 0 0 1 16 0M72 88a8 8 0 0 1 16 0"/></g></svg>
  <svg class="abs" style="left:722px;top:420px" width="90" height="12"><path d="M0 6h80" stroke="#999" stroke-dasharray="3 3"/><path d="M78 1l8 5-8 5" fill="#999"/></svg>
  <svg class="step-ring abs" style="left:860px" viewBox="0 0 120 120"><circle cx="60" cy="60" r="54" fill="#f1f1f3"/><path d="M60 4a56 56 0 0 1 40 95" fill="none" stroke="#f05a28" stroke-width="2"/><path d="M20 100A56 56 0 0 1 40 8" fill="none" stroke="#f05a28" stroke-width="2"/><g fill="none" stroke="#444" stroke-width="1.8"><path d="M44 86V50M60 86V38M76 86V50M38 56l6-8 6 8M54 44l6-8 6 8M70 56l6-8 6 8"/><circle cx="46" cy="78" r="7"/><circle cx="74" cy="78" r="7"/></g></svg>

  <p class="step-label abs" style="left:158px">Step 1</p>
  <p class="step-text abs" style="left:163px">Schedule an appointment to go through the basics of what you need and to find out if we are a good fit to work together</p>
  <p class="step-label abs" style="left:470px">Step 2</p>
  <p class="step-text abs" style="left:475px">Work with our team to build out your customer journey and selling system</p>
  <p class="step-label abs" style="left:778px">Step 3</p>
  <p class="step-text abs" style="left:813px;width:210px">Execute and enjoy the extra revenue!</p>

  <p class="abs center" style="top:632px;font-size:15px;color:var(--ink)">So, Schedule Your Appointment Today.</p>
  <p class="abs" style="left:165px;width:870px;top:664px;text-align:center;font-size:15px;line-height:25px">And in the meantime, checkout our Chatterly ads checklist. So you can stop any poor running campaigns and fill in the gaps where they are needed.</p>
  <a class="btn btn-orange" style="left:526px;top:728px;width:162px;height:40px;font-size:18px"><span class="dot"></span>Get Started</a>
</section>

<section class="testimonials" role="img" aria-label="Dim photo of a team working in an office">
  <h2 class="abs center" style="top:80px">What Others Are Saying...</h2>
  <div class="rule" style="top:133px"></div>

  <div class="slider-arrow abs" style="left:79px;background:#8a8d93;color:#ddd">◀</div>
  <div class="slider-arrow abs" style="left:1080px;background:var(--white);color:#888">▶</div>

  <article class="quote-card abs" style="left:141px">
    <span class="qm">&ldquo;</span><span class="avatar" role="img" aria-label="Client portrait"></span>
    <p>Lorem ipsum dolor sit amet, consec adipiscing elit, sed diam nonummy nibh euismod tincidunt ut laoreet dolore magna aliquam erat volutpat. Ut wisi enim ad minim veniam, quis nostrud exerci tation.</p>
    <span class="name-tag">Mara, Quill</span><span class="stars">★★★★<span class="off">☆</span></span>
  </article>
  <article class="quote-card abs" style="left:452px">
    <span class="qm">&ldquo;</span><span class="avatar" role="img" aria-label="Client portrait"></span>
    <p>Lorem ipsum dolor sit amet, consec adipiscing elit, sed diam nonummy nibh euismod tincidunt ut laoreet dolore magna aliquam erat volutpat. Ut wisi enim ad minim veniam, quis nostrud exerci tation.</p>
    <span class="name-tag">Tessa Lorne</span><span class="stars">★★★★★</span>
  </article>
  <article class="quote-card abs" style="left:762px">
    <span class="qm">&ldquo;</span><span class="avatar" role="img" aria-label="Client portrait"></span>
    <p>Lorem ipsum dolor sit amet, consec adipiscing elit, sed diam nonummy nibh euismod tincidunt ut laoreet dolore magna aliquam erat volutpat. Ut wisi enim ad minim veniam, quis nostrud exerci tation.</p>
    <span class="name-tag">Ravi Ondell</span><span class="stars">★★★★<span class="off">☆</span></span>
  </article>
</section>

<section class="why">
  <h2 class="section-title abs center" style="top:72px">Why Choose Us</h2>
  <div class="rule" style="top:122px"></div>

  <article class="why-card abs" style="left:141px">
    <div class="why-icon"><svg width="50" height="50" viewBox="0 0 50 50" fill="none" stroke="#222" stroke-width="2.5"><rect x="7" y="10" width="36" height="32" rx="2"/><path d="M7 18h36M15 6v8M35 6v8"/><path d="M14 25h4M23 25h4M32 25h4M14 32h4M23 32h4M32 32h4" stroke-width="3"/></svg></div>
    <h3>Month-to-month</h3>
    <p>Lorem ipsum dolor sit amet, consectetuer adipiscing elit, sed diam nonummy nibh euismod dolor sit amet, consectetuer adipiscing elit, sed diam.</p>
  </article>
  <article class="why-card abs" style="left:458px">
    <div class="why-icon"><svg width="50" height="50" viewBox="0 0 50 50" fill="none" stroke="#222" stroke-width="2.5"><rect x="11" y="8" width="28" height="36" rx="2"/><path d="M19 8V5h12v3M18 18h14M18 24h14M18 30h8"/><circle cx="33" cy="36" r="6"/></svg></div>
    <h3>No long-term Contracts</h3>
    <p>Lorem ipsum dolor sit amet, consectetuer adipiscing elit, sed diam nonummy nibh euismod dolor sit amet, consectetuer adipiscing elit, sed diam.</p>
  </article>
  <article class="why-card abs" style="left:775px">
    <div class="why-icon"><svg width="50" height="50" viewBox="0 0 50 50" fill="none" stroke="#222" stroke-width="2.5"><circle cx="20" cy="10" r="5"/><path d="M14 44V20h12v24M20 20v12"/><circle cx="33" cy="35" r="7"/><path d="M30 35l2 2 4-4"/></svg></div>
    <h3>Cheaper than hiring in-house</h3>
    <p>Lorem ipsum dolor sit amet, consectetuer adipiscing elit, sed diam nonummy nibh euismod dolor sit amet, consectetuer adipiscing elit, sed diam.</p>
  </article>

  <a class="btn btn-dark" style="left:482px;top:437px;width:235px;height:41px"><span class="dot"></span>Schedule Appointment</a>
</section>

<footer class="site-footer" role="img" aria-label="Dark aerial photo of a city at night">
  <h4 class="abs" style="left:138px;top:62px">Quick Links</h4>
  <ul class="abs" style="left:138px;top:100px"><li>Home</li><li>About</li><li>Case Studies</li><li>Contact Us</li></ul>
  <h4 class="abs" style="left:287px;top:62px">Other Links</h4>
  <ul class="abs" style="left:287px;top:100px"><li>Lorem Ispum</li><li>Lorem Ispum</li><li>Lorem Ispum</li><li>Lorem Ispum</li></ul>
  <h4 class="abs" style="left:486px;top:62px">Contact Details</h4>

  <div class="contact-item abs" style="left:486px;top:108px">
    <svg width="18" height="24" viewBox="0 0 18 24" fill="none" stroke="#3b82d6" stroke-width="2"><path d="M9 23s8-9 8-14A8 8 0 0 0 1 9c0 5 8 14 8 14z"/><circle cx="9" cy="9" r="3"/></svg>
    <span>Street Name, City Name<br>State Zipcode</span>
  </div>
  <div class="contact-item abs" style="left:697px;top:114px">
    <svg width="20" height="20" viewBox="0 0 20 20" fill="none" stroke="#3b82d6" stroke-width="2"><rect x="1" y="4" width="18" height="13"/><path d="M1 4l9 7 9-7"/></svg>
    <span>Email Us<br>inquiry@orchiddigital.com</span>
  </div>
  <div class="contact-item abs" style="left:911px;top:114px">
    <svg width="20" height="20" viewBox="0 0 20 20" fill="none" stroke="#3b82d6" stroke-width="2"><path d="M4 1l4 4-2 3c1 3 3 5 6 6l3-2 4 4-3 3C8 19 1 12 1 4z"/></svg>
    <span>Call Us<br>123.456.7890</span>
  </div>

  <div class="brand abs" style="left:486px;top:184px;color:var(--white);font-size:26px"><span class="mark"></span>ORCHIDDIGITAL</div>
  <div class="abs" style="left:810px;top:188px;display:flex;align-items:center;gap:4px;color:var(--white);font-size:13px">
    <span style="margin-right:4px">Follow Us On</span>
    <span class="social"></span><span class="social"></span><span class="social"></span>
  </div>
</footer>

<div class="copyright">Copyright © 2020 OrchidDigital. All Rights Reserved. Terms of Service &nbsp; | &nbsp; Privacy Policy</div>

</body>
</html>
```